Eye catching business card

2 sided
Black background with logo in color on one side along with the words "Proudly serving the commercial and defense industries since 1975"
2nd side to contain contact information (see attached current business card) and "Waterjet, Composite, Precision Machining and Clean Room Manufacturing" with a very faint watermark of a waving USA Flag in the back ground.
Remove the "est. 195" from the current logo design

```html
<!DOCTYPE html>
<html lang="en">
<head>
<meta charset="utf-8">
<title>Allegheny Precision Works – Business Card</title>
<link href="https://fonts.googleapis.com/css2?family=Cabin:ital,wght@0,400;0,500;0,600;0,700;1,700&family=Montserrat:wght@500;600&display=swap" rel="stylesheet">
<style>
  :root {
    --page: #ffffff;
    --black-1: #1b1b1b;
    --black-2: #2a2a2a;
    --steel-1: #e4e4e4;
    --steel-2: #c9c9c9;
    --grey-text: #8e8e8e;
    --grey-band: #9a9a9a;
    --ink: #3a3a3a;
    --contact: #6f6f6f;
    --blue-1: #1d5d9a;
    --blue-2: #1a4f8a;
    --blue-3: #16377e;
    --brand-blue: #2a8fe0;
    --white: #ffffff;
  }
  * { box-sizing: border-box; margin: 0; padding: 0; }
  html, body { width: 1200px; height: 1200px; overflow: hidden; background: var(--page); }
  body { position: relative; font-family: "Cabin", sans-serif; }

  .card { position: absolute; left: 251px; width: 705px; height: 403px; overflow: hidden; }

  /* Front */
  .card--front {
    top: 169px;
    background:
      repeating-linear-gradient(90deg, rgba(255,255,255,0.035) 0 1px, transparent 1px 3px, rgba(0,0,0,0.15) 3px 4px, transparent 4px 7px),
      linear-gradient(180deg, var(--black-2), var(--black-1));
  }
  .front-mark {
    position: absolute; left: 50%; top: 108px; transform: translateX(-50%);
    width: 96px; height: 96px; background: var(--brand-blue);
  }
  .front-name {
    position: absolute; left: 0; right: 0; top: 236px; text-align: center;
    font-family: "Montserrat", sans-serif; font-weight: 600; font-size: 31px;
    letter-spacing: 1px; color: var(--grey-text);
  }
  .front-rule {
    position: absolute; left: 176px; right: 176px; top: 293px; height: 2px; background: var(--grey-text);
  }
  .tagline-band {
    position: absolute; left: 0; right: 0; top: 327px; height: 25px; background: var(--grey-band);
    display: flex; align-items: center; justify-content: center;
    font-size: 14px; font-weight: 500; color: var(--ink); letter-spacing: -0.3px;
  }

  /* Back */
  .card--back {
    top: 611px;
    background:
      repeating-linear-gradient(90deg, rgba(255,255,255,0.25) 0 1px, transparent 1px 3px, rgba(0,0,0,0.04) 3px 4px, transparent 4px 6px),
      linear-gradient(180deg, var(--steel-1), var(--steel-2));
  }
  .flag-watermark {
    position: absolute; left: 0; top: 0; width: 292px; height: 222px;
    background:
      radial-gradient(ellipse at 20% 15%, rgba(110,120,170,0.35), transparent 55%),
      linear-gradient(160deg, rgba(200,110,120,0.22), rgba(230,230,230,0) 80%);
  }
  .back-brand {
    position: absolute; right: 56px; top: 34px; width: 160px; text-align: center;
  }
  .back-brand .mark { width: 30px; height: 30px; margin: 0 auto 8px; background: var(--grey-text); }
  .back-brand .name {
    font-family: "Montserrat", sans-serif; font-weight: 600; font-size: 12px;
    color: var(--grey-text); letter-spacing: 0.5px; line-height: 1.2;
  }
  .name-plate { position: absolute; right: 0; top: 103px; width: 245px; height: 61px; }
  .name-plate__shadow {
    position: absolute; inset: 0; border-radius: 31px 0 0 31px; background: #8b8b8b;
  }
  .name-plate__body {
    position: absolute; left: 7px; right: 0; top: 0; bottom: 0; border-radius: 31px 0 0 31px;
    background: linear-gradient(90deg, var(--blue-1), var(--blue-2) 55%, var(--blue-3));
    color: var(--white); text-align: right; padding: 6px 40px 0 0;
  }
  .person-name { font-size: 30px; font-weight: 500; line-height: 1.1; }
  .person-name em { font-style: italic; font-weight: 700; }
  .person-title { font-size: 15px; font-weight: 500; }

  .services-band {
    position: absolute; left: 0; right: 0; top: 268px; height: 29px;
    background: linear-gradient(90deg, var(--blue-2), var(--blue-1) 50%, var(--blue-3));
    color: var(--white); display: flex; align-items: center; justify-content: center;
    font-size: 16px; font-weight: 500; letter-spacing: -0.3px;
  }
  .contacts { position: absolute; left: 0; right: 0; top: 305px; font-size: 16px; color: var(--contact); }
  .contacts__row { display: flex; justify-content: center; gap: 26px; height: 26px; align-items: center; }
  .contact { display: flex; align-items: center; gap: 5px; letter-spacing: -0.2px; }
  .contact svg { width: 15px; height: 15px; flex: none; }
</style>
</head>
<body>

<section class="card card--front">
  <div class="front-mark"></div>
  <div class="front-name">ALLEGHENY PRECISION WORKS</div>
  <div class="front-rule"></div>
  <div class="tagline-band">Proudly serving the commercial and defense industries since 1975</div>
</section>

<section class="card card--back">
  <div class="flag-watermark" role="img" aria-label="Faint waving United States flag watermark"></div>

  <div class="back-brand">
    <div class="mark"></div>
    <div class="name">ALLEGHENY PRECISION WORKS</div>
  </div>

  <div class="name-plate">
    <div class="name-plate__shadow"></div>
    <div class="name-plate__body">
      <div class="person-name">Dale <em>Morrow</em></div>
      <div class="person-title">President</div>
    </div>
  </div>

  <div class="services-band">Waterjet, Composite, Precision Machining and Clean Room Manufacturing</div>

  <div class="contacts">
    <div class="contacts__row">
      <span class="contact">
        <svg viewBox="0 0 16 16"><circle cx="8" cy="8" r="8" fill="#6f6f6f"/><path d="M5.5 4.5l1.5-.5 1 2-1 .8a5 5 0 0 0 2.2 2.2l.8-1 2 1-.5 1.5c-3 .4-6.4-3-6-6z" fill="#fff"/></svg>
        555-014-2200
      </span>
      <span class="contact">
        <svg viewBox="0 0 16 16"><circle cx="8" cy="8" r="8" fill="#6f6f6f"/><rect x="5" y="4" width="6" height="3" fill="#fff"/><rect x="4" y="7" width="8" height="4" rx="1" fill="#fff"/><rect x="5.5" y="9" width="5" height="3" fill="#6f6f6f" stroke="#fff" stroke-width=".8"/></svg>
        Fax: 555-014-2201
      </span>
    </div>
    <div class="contacts__row">
      <span class="contact">
        <svg viewBox="0 0 16 16"><circle cx="8" cy="8" r="7.3" fill="none" stroke="#6f6f6f" stroke-width="1.3"/><rect x="4" y="5.5" width="8" height="5.5" fill="none" stroke="#6f6f6f"/><path d="M4 5.5l4 3 4-3" fill="none" stroke="#6f6f6f"/></svg>
        dale@alleghenyworks.com
      </span>
      <span class="contact">
        <svg viewBox="0 0 16 16"><circle cx="8" cy="8" r="7.3" fill="none" stroke="#6f6f6f" stroke-width="1.3"/><rect x="4" y="5.5" width="8" height="5.5" fill="none" stroke="#6f6f6f"/><path d="M4 5.5l4 3 4-3" fill="none" stroke="#6f6f6f"/></svg>
        info@alleghenyworks.com
      </span>
      <span class="contact">
        <svg viewBox="0 0 16 16"><circle cx="8" cy="8" r="7.3" fill="none" stroke="#6f6f6f" stroke-width="1.3"/><circle cx="8" cy="8" r="4.5" fill="none" stroke="#6f6f6f" stroke-width=".8"/><ellipse cx="8" cy="8" rx="2" ry="4.5" fill="none" stroke="#6f6f6f" stroke-width=".8"/><path d="M3.5 8h9" stroke="#6f6f6f" stroke-width=".8"/></svg>
        www.alleghenyworks.com
      </span>
    </div>
    <div class="contacts__row">
      <span class="contact">
        <svg viewBox="0 0 16 16"><circle cx="8" cy="8" r="8" fill="#6f6f6f"/><path d="M8 3.5a3 3 0 0 1 3 3c0 2.2-3 5.8-3 5.8S5 8.7 5 6.5a3 3 0 0 1 3-3z" fill="#fff"/><circle cx="8" cy="6.5" r="1.1" fill="#6f6f6f"/></svg>
        412 Mill Creek Rd. Hanover Falls, PA 17000
      </span>
    </div>
  </div>
</section>

</body>
</html>
```